Webdesign für Raumgestalter / Interior Designer und Implementierung
Zielgruppe
Wir möchten zukünftig für Menschen «Träume in Räume» verwandeln und sind spezialisiert auf Interior Design, ReDesign Home Staging wie auch Dekorationen mit folgenden Leistungen an:
- Interior Design
- Home Styling
- Home Staging
- Dekoration
Aufgabenstellung
(Wichtig: Bitte Anforderungen und Fotos im PDF File im Anhang beachten)
Aufbau der Homepage
Homepage wird in verschiedenen Seiten/Fenster aufgebaut. Diese können oben auf der Homepage angeklickt werden. Der Aufbau ist in 5 Seiten: Home, Leistungen, Referenzen, Pakete und Preise, Kontakt
- Die Homepage sollte dann von uns gemanagt werden können. (Bspw. Plattformen oder andere Gremien, wo die Homepage einfach und ohne tiefe Informatikkenntnisse gemanagt werden kann :-).)
- Die Leistungen betreffen Templating inkl. Umsetzung (Online-Fertigstellung), ich kann bei der URL-Verknüpfung unterstützen.
1) Home
Willkommensseite, inspirierend, einladend, sollte die Besucher dazu animieren vertiefter die Detail anzuschauen.
Es soll ein Button unten ermöglichen, ins zweite Fenster «Referenzen» zu klicken. Siehe unteres Kapitel.
2) Leistungen
a. Interior Design
b. Home Styling
c. Home Staging
d. Dekoration
Hier wird der Ablauf von Projekten aufgezeigt, dieser bildet sich in:
- Planung, Designen, Realisieren
Weiterer sollen realisierte Design-Projekte von bspw. Räumen mit Fotos aufgeführt sein.
3) Referenzen
- Dieses Fenster soll das Interesse möglicher Kunden im Detail erwecken
- Es soll ein erster Termin telefonisch oder per Videocall stattfinden können
(dient zum Kennenlernen, Bedürfnisse verstehen, Ablauf aufzeigen)
4) Pakete und Preise
Hier werden die Pakete und Preise beschrieben.
Die Preise werden auf Rapportsbasis erstellt und richten sich nach Offerten und Wünschen des Kunden. Preis ist bei 80 Franken pro Stunde, das erste Beratungsgespräch wird nicht verrechnet.
Hier können Details in einer Tabelle / Preisliste erarbeitet werden:
- Private Wohnräume
o Private Wohnung
o Privates Haus
o Ferienimmobilien
- Business Einrichtungen
o Einrichtungen von Geschäften
o NestoFlat-Einrichtungen
o ReDesign für Verkauf von Immo..

```html
<!DOCTYPE html>
<html lang="de">
<head>
<meta charset="utf-8">
<title>Raumwerk – Träume in Räume</title>
<link rel="stylesheet" href="https://fonts.googleapis.com/css2?family=Oswald:wght@300&family=Raleway:wght@400;600&family=Mrs+Saint+Delafield&display=swap">
<style>
  :root {
    --sand: #dccdc4;
    --blush: #e9dcd3;
    --ink: #262626;
    --paper: #ffffff;
    --stage: #f4f4f4;
    --line: #2b2b2b;
    --muted: #6b6b6b;
  }
  * { margin: 0; padding: 0; box-sizing: border-box; }
  html, body { width: 1200px; height: 4250px; overflow: hidden; }
  body { background: var(--stage); position: relative; font-family: "Raleway", sans-serif; color: var(--ink); }

  .page {
    position: absolute; left: 75px; top: 110px; width: 1050px; height: 3370px;
    background: var(--paper); overflow: hidden;
    box-shadow: 0 30px 50px rgba(0,0,0,.35);
  }
  .page > * { position: absolute; }

  .backdrop { left: 0; top: 0; width: 1050px; height: 3370px; }

  .photo { display: block; }

  /* hero */
  .hero-photo { left: 0; top: 0; width: 1050px; height: 590px;
    background: linear-gradient(90deg, #e3d0c4 0%, #ecdfd6 35%, #f2e9e3 55%, #e6d6cc 80%, #ead9cf 100%); }
  .brand-box { left: 474px; top: 0; width: 98px; height: 70px; background: var(--paper);
    display: flex; align-items: flex-end; justify-content: center; padding-bottom: 12px; }
  .brand-name { font-family: "Raleway", sans-serif; font-weight: 400; font-size: 13px; letter-spacing: 2px; color: var(--ink); }
  .menu-icon { left: 980px; top: 8px; width: 40px; height: 36px; }
  .hero-title { left: 0; top: 170px; width: 1050px; text-align: center; font-weight: 400;
    font-family: "Mrs Saint Delafield", cursive; font-size: 160px; line-height: 1; color: rgba(255,255,255,.85); }

  .btn { font-family: "Raleway", sans-serif; font-size: 9px; letter-spacing: .5px; text-transform: uppercase;
    display: flex; align-items: center; justify-content: center; height: 26px; width: 124px; }
  .btn-dark { background: var(--ink); color: var(--paper); }
  .btn-sand { background: var(--sand); color: var(--paper); }
  .btn-light { background: var(--paper); color: var(--ink); }

  .chevron { width: 60px; height: 28px; }

  /* service blocks */
  .frame { border: 1px solid var(--line); }
  .service-title { font-family: "Oswald", sans-serif; font-weight: 300; font-size: 78px; line-height: 1; color: var(--ink); }
  .service-text { font-family: "Raleway", sans-serif; font-size: 10.5px; line-height: 14px; color: var(--ink); text-align: justify; }

  /* interior design */
  .interior-frame { left: 22px; top: 718px; width: 650px; height: 336px; }
  .interior-title { left: 44px; top: 762px; }
  .interior-text { left: 44px; top: 904px; width: 460px; }
  .interior-lamp { left: 672px; top: 636px; width: 346px; height: 466px;
    background: linear-gradient(160deg, #4b4d50 0%, #6b6c6e 45%, #8a6a52 80%, #a97d5c 100%); }
  .interior-chair { left: 566px; top: 680px; width: 210px; height: 320px;
    background: linear-gradient(180deg, #efecea 0%, #d9d4cf 55%, #8f7c6b 100%); }
  .interior-btn { left: 220px; top: 1078px; }

  /* home styling */
  .styling-cushions { left: 0; top: 1222px; width: 260px; height: 390px;
    background: linear-gradient(170deg, #e9e2db 0%, #d8b9ae 40%, #b69081 70%, #8b7263 100%); }
  .styling-plant { left: 152px; top: 1430px; width: 210px; height: 316px;
    background: linear-gradient(180deg, #f1efec 0%, #c9c4b8 45%, #6f7a5c 75%, #3e4a3a 100%); }
  .styling-frame { left: 388px; top: 1220px; width: 680px; height: 334px; }
  .styling-title { left: 406px; top: 1262px; }
  .styling-text { left: 410px; top: 1404px; width: 460px; }
  .styling-btn { left: 586px; top: 1580px; }

  /* home staging */
  .staging-title { left: 274px; top: 1892px; }
  .staging-text { left: 286px; top: 2038px; width: 466px; }
  .staging-btn { left: 464px; top: 2212px; }

  /* dekoration */
  .deco-shelf { left: 630px; top: 2370px; width: 388px; height: 568px;
    background: linear-gradient(180deg, #eef0f1 0%, #e2e2e0 60%, #d8b49a 85%, #c9977a 100%); }
  .deco-glass { left: 494px; top: 2422px; width: 222px; height: 330px;
    background: linear-gradient(170deg, #b08f76 0%, #d7c8bb 45%, #f0ebe7 100%); }
  .deco-frame { left: 42px; top: 2486px; width: 804px; height: 334px; }
  .deco-title { left: 58px; top: 2528px; }
  .deco-text { left: 62px; top: 2670px; width: 420px; }
  .deco-btn { left: 240px; top: 2846px; }

  /* call to action */
  .cta-band { left: 0; top: 2954px; width: 1050px; height: 262px; background: var(--ink); }
  .cta-title { left: 44px; top: 2994px; font-family: "Oswald", sans-serif; font-weight: 300;
    font-size: 80px; line-height: 100px; color: var(--blush); }
  .cta-tile { left: 692px; top: 3066px; width: 166px; height: 150px; background: var(--sand); }
  .cta-arrow { left: 808px; top: 3104px; width: 36px; height: 74px; }
  .cta-label { left: 712px; top: 3178px; font-size: 8px; line-height: 11px; text-transform: uppercase; color: var(--ink); }

  /* footer */
  .site-footer { left: 0; top: 3216px; width: 1050px; height: 154px; background: var(--sand); }
  .footer-brand { left: 0; top: 3246px; width: 1050px; text-align: center;
    font-family: "Raleway", sans-serif; font-size: 16px; letter-spacing: 3px; color: var(--ink); }
  .footer-address { left: 44px; top: 3286px; font-size: 8px; color: var(--ink); }
  .footer-social { left: 966px; top: 3272px; display: flex; gap: 6px; }
  .footer-social span { width: 20px; height: 20px; border: 1.5px solid var(--ink); display: block; }
  .footer-legal { left: 0; top: 3346px; width: 1050px; text-align: center; font-size: 8px; color: var(--ink); }

  /* style sheet row */
  .swatch { position: absolute; top: 3620px; width: 162px; height: 162px; }
  .swatch-sand { left: 60px; background: var(--sand); }
  .swatch-ink { left: 382px; background: var(--ink); }
  .type-sample { position: absolute; left: 736px; color: #1e1e1e; line-height: 1.2; }
  .type-raleway { top: 3606px; font-family: "Raleway", sans-serif; font-size: 34px; }
  .type-oswald { top: 3660px; font-family: "Oswald", sans-serif; font-weight: 300; font-size: 36px; }
  .type-script { top: 3722px; font-family: "Mrs Saint Delafield", cursive; font-size: 60px; line-height: 1; }
</style>
</head>
<body>

<main class="page">
  <svg class="backdrop" viewBox="0 0 1050 3370" width="1050" height="3370" aria-hidden="true">
    <polygon points="1050,962 1050,1596 0,1986 0,1352" fill="var(--sand)"/>
    <line x1="530" y1="1794" x2="1050" y2="1978" stroke="var(--line)" stroke-width="1.2"/>
    <line x1="0" y1="2102" x2="752" y2="2370" stroke="var(--line)" stroke-width="1.2"/>
    <line x1="1020" y1="2470" x2="1050" y2="2482" stroke="var(--line)" stroke-width="1.2"/>
  </svg>

  <!-- hero -->
  <div class="photo hero-photo" role="img" aria-label="Helles Wohnzimmer mit dunklem Sofa, Couchtisch und Vase mit Trockengräsern"></div>
  <div class="brand-box"><span class="brand-name">RAUMWERK</span></div>
  <svg class="menu-icon" viewBox="0 0 40 36" aria-label="Menü">
    <g fill="#ffffff">
      <circle cx="6" cy="6" r="3.5"/><circle cx="20" cy="6" r="3.5"/><circle cx="34" cy="6" r="3.5"/>
      <circle cx="6" cy="18" r="3.5"/><circle cx="20" cy="18" r="3.5"/><circle cx="34" cy="18" r="3.5"/>
      <circle cx="6" cy="30" r="3.5"/><circle cx="20" cy="30" r="3.5"/><circle cx="34" cy="30" r="3.5"/>
    </g>
  </svg>
  <h1 class="hero-title">Träume in Räume</h1>
  <a class="btn btn-dark" style="left:462px;top:508px;">Referenzen</a>
  <svg class="chevron" style="left:494px;top:548px;" viewBox="0 0 60 28" aria-hidden="true">
    <polyline points="2,4 30,24 58,4" fill="none" stroke="#ffffff" stroke-width="2"/>
  </svg>

  <!-- interior design -->
  <div class="photo interior-lamp" role="img" aria-label="Dunkle Wand mit schwarzer Pendelleuchte und Ledersofa"></div>
  <div class="photo interior-chair" role="img" aria-label="Weisser Sessel mit Schaffell vor einem schwarzen Bild"></div>
  <div class="frame interior-frame"></div>
  <h2 class="service-title interior-title">Interior Design</h2>
  <p class="service-text interior-text">Wir planen Räume, die zu Ihrem Leben passen. Gemeinsam klären wir Ihre Wünsche, Ihren Alltag und Ihr Budget. Danach entwickeln wir ein stimmiges Konzept aus Farben, Materialien, Licht und Möbeln. Jede Entscheidung wird sorgfältig abgestimmt, damit Funktion und Atmosphäre zusammenfinden. Von der ersten Skizze bis zur fertigen Umsetzung begleiten wir Sie persönlich und zuverlässig. Wir koordinieren Handwerker, Lieferanten und Termine, damit Sie sich entspannt zurücklehnen können. So entsteht ein Zuhause, das Ruhe ausstrahlt, Ihre Persönlichkeit zeigt und jeden Tag Freude bereitet. Lassen Sie sich inspirieren und entdecken Sie, was in Ihren Räumen steckt.</p>
  <a class="btn btn-sand interior-btn">Mehr erfahren</a>
  <svg class="chevron" style="left:494px;top:1150px;" viewBox="0 0 60 28" aria-hidden="true">
    <polyline points="2,4 30,24 58,4" fill="none" stroke="var(--ink)" stroke-width="2"/>
  </svg>

  <!-- home styling -->
  <div class="photo styling-cushions" role="img" aria-label="Sofa mit Kissen in Rosé, Weiss und Bordeaux"></div>
  <div class="photo styling-plant" role="img" aria-label="Grüner Sessel mit Zimmerpflanze und rundem Spiegel"></div>
  <div class="frame styling-frame"></div>
  <h2 class="service-title styling-title">Home Styling</h2>
  <p class="service-text styling-text">Mit wenigen gezielten Eingriffen verwandeln wir bestehende Räume in neue Lieblingsorte. Wir arbeiten mit dem, was Sie bereits besitzen, und ergänzen passende Stücke, Textilien, Pflanzen und Accessoires. Farben und Formen werden harmonisch kombiniert, damit ein ruhiges Gesamtbild entsteht. Kleine Veränderungen an Licht und Anordnung bewirken oft erstaunlich viel. Wir hören zu, beraten ehrlich und respektieren Ihren persönlichen Stil. Das Ergebnis ist ein Zuhause, das frisch, wohnlich und ganz nach Ihrem Geschmack wirkt. Ideal für alle, die ohne grossen Umbau ein neues Wohngefühl erleben möchten und dabei Wert auf Qualität legen.</p>
  <a class="btn btn-light styling-btn">Mehr erfahren</a>
  <svg class="chevron" style="left:494px;top:1746px;" viewBox="0 0 60 28" aria-hidden="true">
    <polyline points="2,4 30,24 58,4" fill="none" stroke="var(--ink)" stroke-width="2"/>
  </svg>

  <!-- home staging -->
  <h2 class="service-title staging-title">Home Staging</h2>
  <p class="service-text staging-text">Beim Verkauf oder bei der Vermietung zählt der erste Eindruck. Wir inszenieren Ihre Immobilie so, dass Interessenten sich sofort wohlfühlen und das Potenzial der Räume erkennen. Leere Zimmer werden mit Möbeln und Dekoration eingerichtet, bewohnte Räume werden neutral und einladend gestaltet. Professionelle Fotos profitieren von klaren Linien, warmem Licht und stimmigen Details. So verkürzt sich die Vermarktungszeit und der Wert Ihres Objekts wird sichtbar. Wir übernehmen Planung, Lieferung, Aufbau und Abholung. Sie erhalten eine transparente Offerte und eine verlässliche Begleitung bis zum erfolgreichen Abschluss.</p>
  <a class="btn btn-dark staging-btn">Mehr erfahren</a>
  <svg class="chevron" style="left:494px;top:2330px;" viewBox="0 0 60 28" aria-hidden="true">
    <polyline points="2,4 30,24 58,4" fill="none" stroke="var(--ink)" stroke-width="2"/>
  </svg>

  <!-- dekoration -->
  <div class="photo deco-shelf" role="img" aria-label="Helle Wand mit Holzregalen, Vasen, Stuhl und Trockengräsern"></div>
  <div class="photo deco-glass" role="img" aria-label="Weingläser und Vase mit Baumwollzweigen"></div>
  <div class="frame deco-frame"></div>
  <h2 class="service-title deco-title">Dekoration</h2>
  <p class="service-text deco-text">Dekoration gibt einem Raum seine Seele. Wir wählen Vasen, Kissen, Bilder, Leuchten und Pflanzen, die Ihre Einrichtung abrunden und Geschichten erzählen. Ob saisonale Akzente, festliche Anlässe oder dauerhafte Gestaltung, wir finden die passenden Stücke und setzen sie gekonnt in Szene. Natürliche Materialien, sanfte Farbtöne und feine Texturen schaffen eine warme, zeitlose Stimmung. Auf Wunsch stellen wir eine Auswahl zusammen, die Sie bequem selbst platzieren können. Oder wir übernehmen alles für Sie, vom Einkauf bis zum letzten Handgriff. So wird jeder Raum zu einem Ort, an dem Sie gerne verweilen.</p>
  <a class="btn btn-sand deco-btn">Mehr erfahren</a>

  <!-- call to action -->
  <section class="cta-band"></section>
  <h2 class="cta-title">Wir erfüllen Ihnen<br>ihren Wohntraum</h2>
  <div class="cta-tile"></div>
  <svg class="cta-arrow" viewBox="0 0 36 74" aria-hidden="true">
    <polyline points="4,2 32,37 4,72" fill="none" stroke="var(--ink)" stroke-width="2"/>
  </svg>
  <span class="cta-label">Termin<br>vereinbaren</span>

  <!-- footer -->
  <footer class="site-footer"></footer>
  <div class="footer-brand">RAUMWERK</div>
  <p class="footer-address">© 2020 Raumwerk | Lindenweg 4 | 6000 Musterdorf</p>
  <div class="footer-social" aria-label="Soziale Netzwerke"><span></span><span></span></div>
  <p class="footer-legal">Datenschutz | Impressum</p>
</main>

<div class="swatch swatch-sand" aria-label="Farbe Sand"></div>
<div class="swatch swatch-ink" aria-label="Farbe Anthrazit"></div>
<p class="type-sample type-raleway">Raleway Regular</p>
<p class="type-sample type-oswald">Oswald Light</p>
<p class="type-sample type-script">Mrs Saint Delafield</p>

</body>
</html>
```